Brume d'Orvelle Hand Crafted Candles promotional flyer

Hand Crafted Soy Candles - I need a flyer to promote my candles and to give information on care of candles.I want this to use the design and colours I already have for my labels and the photo I have attached.I am aiming at a sophisticated market so would like to reflect this in the design.
Should appeal to sophisticated women who enjoy the pleasure of candles - to enhance their enjoyment of life - gives them the 'brume d'orvelle'.
the candles are hand crafted from all natural ingredients, environmentally friendly and with exquisite fragrances

Target Market(s)

sophisticated females

Industry/Entity Type

Promotional

Font styles to use
Script

Colors
cfeae6
ecdaeb

Requirements
Must have
• something expressing 'brume d'orvelle' - the enjoyment of candles
Should not have
• bright colours

```html
<!DOCTYPE html>
<html lang="en">
<head>
<meta charset="utf-8">
<title>Brume d'Orvelle Hand Crafted Candles – Flyer</title>
<link href="https://fonts.googleapis.com/css2?family=Pinyon+Script&family=Cinzel:wght@600&family=Tinos:ital,wght@0,400;1,400;1,700&family=Arimo:ital,wght@0,700;1,700&display=swap" rel="stylesheet">
<style>
  :root{
    --page:#4a4a4c;
    --ink:#161616;
    --accent:#2f8fc4;
    --accent-dark:#1f6e9c;
    --sky-light:#e6f1f7;
    --sky:#a9cde1;
    --sky-deep:#7fb2cf;
    --pill:#dcdcdc;
    --silver:#9a9a9a;
    --silver-light:#d8d8d8;
    --table:#3c3d40;
    --table-dark:#2a2b2d;
    --tip-head:#8fc2e0;
    --white:#ffffff;
  }
  *{box-sizing:border-box;margin:0;padding:0}
  html,body{width:1200px;height:2456px;overflow:hidden;background:var(--page)}
  .flyer{
    position:absolute;left:50px;top:447px;width:1100px;height:1562px;overflow:hidden;
    background:linear-gradient(180deg,var(--white) 0%,var(--sky-light) 30%,var(--sky) 62%,var(--sky-deep) 75%);
    font-family:"Tinos",serif;color:var(--ink);
  }
  .filigree-pattern{
    position:absolute;left:0;top:0;width:100%;height:1160px;
    background:radial-gradient(ellipse at 15% 40%,rgba(255,255,255,.45),transparent 45%),
               radial-gradient(ellipse at 85% 60%,rgba(255,255,255,.4),transparent 45%);
  }
  .brand-name{
    position:absolute;top:18px;left:0;width:100%;text-align:center;
    font-family:"Pinyon Script",cursive;font-weight:400;font-size:104px;line-height:1;color:var(--ink);
  }
  .tagline-arc{position:absolute;top:112px;left:200px;width:700px;height:150px;overflow:visible}
  .tagline-arc text{font-family:"Cinzel",serif;font-weight:600;font-size:36px;fill:var(--ink);letter-spacing:1px}
  .scroll-ornament{position:absolute;top:228px;height:190px;width:300px;border-radius:90px 40px 90px 40px;
    background:radial-gradient(ellipse at center,var(--silver-light),var(--silver) 60%,transparent 72%)}
  .scroll-ornament.left{left:115px}
  .scroll-ornament.right{right:115px;transform:scaleX(-1)}
  .medallion{
    position:absolute;left:435px;top:196px;width:230px;height:230px;border-radius:50%;
    border:8px solid var(--silver);
    background:radial-gradient(circle at 50% 40%,#cfe4ef,#6c9fbf 55%,#2f3438 80%);
  }
  .headline{position:absolute;top:438px;left:0;width:100%;text-align:center;
    font-family:"Tinos",serif;font-style:italic;font-weight:700;font-size:32px;line-height:1.1;color:var(--accent)}
  .intro{position:absolute;top:478px;left:0;width:100%;text-align:center;font-style:italic;font-size:29px;line-height:31px}
  .features{
    position:absolute;left:135px;top:590px;width:910px;height:92px;border-radius:46px;background:var(--pill);
    display:grid;grid-template-columns:380px 1fr;align-content:center;padding-left:36px;row-gap:2px;
    font-family:"Tinos",serif;font-size:26px;line-height:1.2;text-transform:uppercase;list-style:none;
  }
  .features li::before{content:"▪ ";}
  .info-column{position:absolute;top:708px}
  .info-column.why{left:58px;width:530px}
  .info-column.refill{left:605px;width:470px}
  .info-column h2{font-family:"Tinos",serif;font-weight:700;font-size:29px;line-height:1.1;color:var(--accent);text-align:center;margin-bottom:6px}
  .info-column ul{padding-left:22px;font-size:23px;line-height:1.0}
  .info-column li{margin-bottom:2px}
  .product-photo{
    position:absolute;left:50px;top:962px;width:900px;height:195px;
    background:linear-gradient(90deg,rgba(30,30,35,.85) 0 22%,rgba(210,200,180,.8) 26% 50%,rgba(235,235,225,.8) 55% 78%,rgba(40,60,150,.75) 82% 92%,transparent 95%);
    border-radius:10px 10px 0 0;
  }
  .care-panel{
    position:absolute;left:0;top:1154px;width:100%;height:408px;
    background:linear-gradient(180deg,var(--table) 0%,var(--table-dark) 100%);
  }
  .care-ribbon{position:absolute;left:22px;top:1162px;transform:rotate(-9deg);
    background:var(--white);border:2px solid var(--accent-dark);padding:5px 26px;
    font-family:"Tinos",serif;font-style:italic;font-size:23px;line-height:1.2;color:var(--accent-dark)}
  .care-tips{position:absolute;left:60px;top:1240px;width:990px;font-family:"Arimo",sans-serif;font-weight:700;color:var(--white)}
  .care-tips h3{font-style:italic;font-size:14px;color:var(--tip-head);margin-bottom:4px;text-transform:uppercase}
  .care-tips ol{list-style:none;counter-reset:tip;font-size:13px;line-height:1.3}
  .care-tips li{counter-increment:tip;position:relative;padding-left:24px;margin-bottom:2px}
  .care-tips li::before{content:counter(tip);position:absolute;left:0;top:1px;width:16px;height:16px;border-radius:50%;
    background:var(--accent);font-size:11px;text-align:center;line-height:16px}
  .contact-bar{position:absolute;left:0;top:1496px;width:1100px;height:48px;background:var(--accent);
    display:flex;justify-content:space-between;align-items:center;padding:0 50px;
    font-family:"Tinos",serif;font-size:27px;color:var(--white)}
  .contact-bar span{display:flex;align-items:center;gap:12px}
  .contact-bar svg{width:26px;height:26px}
</style>
</head>
<body>
<main class="flyer">
  <div class="filigree-pattern" role="img" aria-label="Soft white filigree scroll pattern over pale blue"></div>

  <h1 class="brand-name">Brume d'Orvelle</h1>
  <svg class="tagline-arc" viewBox="0 0 700 150" aria-label="Handcrafted Soy Candles">
    <path id="arc" d="M20 140 Q350 0 680 140" fill="none"/>
    <text><textPath href="#arc" startOffset="50%" text-anchor="middle">HANDCRAFTED SOY CANDLES</textPath></text>
  </svg>

  <div class="scroll-ornament left" role="img" aria-label="Silver baroque scroll ornament"></div>
  <div class="scroll-ornament right" role="img" aria-label="Silver baroque scroll ornament"></div>
  <div class="medallion" role="img" aria-label="Photo of a black soy candle in a round silver frame"></div>

  <p class="headline">AN EXHUBERANT ENJOYMENT OF LIFE</p>
  <p class="intro">These Candles will fill you with “Brume d'Orvelle”!<br>Each handcrafted, soy candle creation is lovingly hand-poured<br>and uses only the finest ingredients and fragrances.</p>

  <ul class="features">
    <li>Completely Non-Toxic</li><li>Clean Burning</li>
    <li>Exquisite Fragrances</li><li>Environmentally Friendly</li>
  </ul>

  <section class="info-column why">
    <h2>Why Soy Wax?</h2>
    <ul>
      <li>Soft, smooth wax that burns clear - no soot or smoke</li>
      <li>Soy Wax Candles burn up to 50% longer than traditional paraffin candles</li>
      <li>Made from soya beans, a renewable natural resource that supports and sustains agriculture - it is biodegradable and environmentally friendly</li>
      <li>Soy Wax burns cooler than paraffin and disperses the fragrance more fully</li>
    </ul>
  </section>
  <section class="info-column refill">
    <h2>Containers Can Be Refilled</h2>
    <ul>
      <li>We offer a refill service - if you return your containers, they can be refilled with the fragrance of your choice</li>
      <li>Or if you have a special container you would like to use for your candle, just contact me for a quote</li>
      <li>We offer a wide range of fragrances - please contact me for details</li>
    </ul>
  </section>

  <div class="product-photo" role="img" aria-label="Photo of four labelled soy candles in black, silver-lidded, clear and blue containers"></div>
  <div class="care-panel" role="img" aria-label="Dark tabletop under the candles"></div>
  <div class="care-ribbon">How to Care for Your Candle</div>

  <section class="care-tips">
    <h3>These tips will ensure you have a long, lasting, fully fragrances candle:</h3>
    <ol>
      <li>When lighting your candle for the first time, allow the wax to melt all the way to the sides of the container - this creates a “memory” and avoids “tunnelling” as the candle burns.</li>
      <li>Always trim the wick to about 6-8mm before re-lighting your candle. This will ensure a long, lasting candle, minimize soot and remove any mushrooming of the wick from a previous burn.</li>
      <li>It is preferable to use a candle “snuffer” to extinguish the flame, or a lid, if the candle has one. Alternatively, you can dip the wick into the melted wax and then straightening. This will stop the wick from smoking and help with relighting.</li>
      <li>All Brume d'Orvelle candles are hand poured, not mass produces - although every effort is made to ensure consistency, every candle may be different.</li>
      <li>Sometimes you may notice darker patches or wet spots - this is not a fault, it is just the natural way the wax has set - it does not affect the candle in any way.</li>
      <li>The top of the candle may also appear slightly uneven - this is just a sign of natural soy wax being hand poured.</li>
      <li>Do not leave your candle in the sunlight, as it may turn a yellowish color - again, this does not affect the candle in any way - it just loses its creamy, white color.</li>
      <li>As these candles contain no preservatives or chemicals, it is recommended that they should be used withing 6 months.</li>
    </ol>
  </section>

  <footer class="contact-bar">
    <span><svg viewBox="0 0 26 26"><rect x="2" y="5" width="22" height="16" rx="2" fill="none" stroke="#fff" stroke-width="2"/><path d="M3 6l10 8 10-8" fill="none" stroke="#fff" stroke-width="2"/></svg>celine.marsh@example.com</span>
    <span><svg viewBox="0 0 26 26"><rect x="7" y="2" width="12" height="22" rx="2" fill="none" stroke="#fff" stroke-width="2"/><rect x="9" y="5" width="8" height="10" fill="#fff"/><circle cx="13" cy="20" r="1.5" fill="#fff"/></svg>0215550198</span>
    <span><svg viewBox="0 0 26 26"><circle cx="13" cy="13" r="10" fill="none" stroke="#fff" stroke-width="2"/><ellipse cx="13" cy="13" rx="4.5" ry="10" fill="none" stroke="#fff" stroke-width="1.6"/><path d="M3 13h20" stroke="#fff" stroke-width="1.6"/></svg>www.mybrumedorvelle.co.nz</span>
  </footer>
</main>
</body>
</html>
```